GILDED BRICKWORK: THE DEPENDABLE ROUTE WHEREBY MODEST HOUSING FLIPS YIELD HANDSOME RETURNS

I am looking for a book cover design for my new E-Book.

My idea for the design is a pin board with before and after photos of our properties pinned on it (example attached). I have also attached some photos to use.

PLEASE SUBMIT OTHER DESIGNS ALSO AS THIS WAS JUST AN IDEA BUT I AM OPEN TO OTHER IDEAS ALSO.

Page size is 5x7 inches

Font styles to use
Serif
Sans Serif

Colors
0255a3
3176b5
85acd3
85cae6
33a6d7
0392cd
9bcb3c
abd036
ec1f27

```html
<!DOCTYPE html>
<html lang="en">
<head>
<meta charset="utf-8">
<title>Gilded Brickwork – E-Book Cover</title>
<link rel="stylesheet" href="https://fonts.googleapis.com/css2?family=Roboto+Condensed:wght@700;800&family=Roboto:wght@900&family=Open+Sans:wght@500&display=swap">
<style>
  :root{
    --page:#ffffff;
    --cover-blue:#6ab2e6;
    --glow:#ffffff;
    --navy:#0e1b4d;
    --band-dark:#0a102e;
    --label-blue:#0e4a7c;
    --white:#ffffff;
    --sky:#8fc4ec;
    --lawn:#5f9a3a;
    --wall:#c9ced3;
    --concrete:#9a9791;
  }
  *{box-sizing:border-box;margin:0;padding:0}
  html,body{width:1200px;height:1000px;overflow:hidden;background:var(--page)}
  .cover{
    position:absolute;left:284px;top:57px;width:632px;height:886px;overflow:hidden;
    background:radial-gradient(ellipse 300px 330px at 300px 520px,var(--glow) 0%,rgba(255,255,255,.55) 35%,rgba(255,255,255,0) 75%),var(--cover-blue);
  }
  .title{position:absolute;left:0;width:100%;text-align:center;font-family:"Roboto Condensed",sans-serif;font-weight:800;line-height:1;letter-spacing:1px}
  .title--top{top:30px;font-size:78px;color:var(--navy)}
  .title--main{top:102px;font-size:104px;color:var(--white)}
  .card{position:absolute;background:var(--white);box-shadow:0 2px 6px rgba(0,0,0,.25)}
  .card__photo{position:absolute;left:0;top:0;width:100%;height:calc(100% - 46px)}
  .card__photo--after{background:linear-gradient(180deg,var(--sky) 0%,var(--sky) 22%,var(--wall) 23%,var(--wall) 60%,var(--lawn) 61%,#4c8a2c 100%)}
  .card__photo--before{background:linear-gradient(180deg,#b9d3e3 0%,#7f8f6a 25%,#b3aa98 55%,var(--concrete) 100%)}
  .card__photo--house{background:linear-gradient(180deg,var(--sky) 0%,#52607c 20%,#4a5672 65%,#8c8b88 66%,#a6a39d 100%)}
  .card__label{position:absolute;left:0;bottom:0;width:100%;height:46px;background:var(--label-blue);color:var(--white);font-family:"Open Sans",sans-serif;font-weight:500;font-size:29px;line-height:46px;text-align:center;letter-spacing:.5px}
  .card--a{left:28px;top:200px;width:200px;height:230px;transform:rotate(12deg)}
  .card--b{left:130px;top:228px;width:232px;height:236px;transform:rotate(-5deg)}
  .card--c{left:395px;top:215px;width:232px;height:236px;transform:rotate(8deg)}
  .card--d{left:-14px;top:450px;width:200px;height:230px;transform:rotate(5deg)}
  .card--e{left:165px;top:462px;width:230px;height:230px;transform:rotate(-3deg)}
  .card--f{left:380px;top:432px;width:240px;height:210px;transform:rotate(-12deg)}
  .subtitle{position:absolute;left:0;top:700px;width:100%;text-align:center;font-family:"Roboto",sans-serif;font-weight:900;font-size:25px;line-height:34px;color:var(--navy);letter-spacing:.5px}
  .subtitle__accent{color:var(--white)}
  .credits{position:absolute;left:0;top:803px;width:100%;height:83px;background:var(--band-dark);color:var(--white);font-family:"Roboto",sans-serif;font-weight:900;font-size:20px;line-height:33px;text-align:center;padding-top:8px;letter-spacing:.5px}
</style>
</head>
<body>
  <main class="cover">
    <h1>
      <span class="title title--top">GILDED</span>
      <span class="title title--main">BRICKWORK</span>
    </h1>

    <div class="card card--a"><div class="card__photo card__photo--before" role="img" aria-label="Old house with verandah and overgrown fence before renovation"></div><div class="card__label">BEFORE</div></div>
    <div class="card card--c"><div class="card__photo card__photo--house" role="img" aria-label="Renovated two-storey grey house with garage after renovation"></div><div class="card__label">AFTER</div></div>
    <div class="card card--b"><div class="card__photo card__photo--after" role="img" aria-label="Renovated white cottage on green lawn after renovation"></div><div class="card__label">AFTER</div></div>
    <div class="card card--f"><div class="card__photo card__photo--before" role="img" aria-label="Dated two-storey house with concrete driveway before renovation"></div><div class="card__label">BEFORE</div></div>
    <div class="card card--d"><div class="card__photo card__photo--before" role="img" aria-label="Tired house with dry yard before renovation"></div><div class="card__label">BEFORE</div></div>
    <div class="card card--e"><div class="card__photo card__photo--after" role="img" aria-label="Renovated house with deck and stepping-stone lawn after renovation"></div><div class="card__label">AFTER</div></div>

    <p class="subtitle">THE DEPENDABLE ROUTE WHEREBY<br><span class="subtitle__accent">MODEST HOUSING FLIPS YIELD</span><br>HANDSOME RETURNS</p>

    <footer class="credits">CREATED AND WRITTEN BY MARCUS TENNANT<br>TENNANT DWELLINGS + READY SET REBUILD</footer>
  </main>
</body>
</html>
```